TLPB Business Card Design

Business card for sole operator professional civil and traffic engineer.
Clients are developers and planners who require assistance with traffic strategic master planning advice and design development for access and infrastructure associated with the development.
Colours already in use are greens for the business name and black for other legend. The attached file shows the letterhead template which is currently in use.
Target Market(s)
Professional Clients in development industry
Most clients known to the Principal and card is mostly required to allow ongoing contact
Industry/Entity Type
Business
Contact Information for Business Card
DESMOND HALVERTON CONSULTING SERVICES
ABN 37 818 502 194
PO Box 871 KERRAWAY NSW 2619
Desmond Halverton 0431 558 906
desmond.halverton@quillmarsh.net

```html
<!DOCTYPE html>
<html lang="en">
<head>
<meta charset="utf-8">
<title>Desmond Halverton Consulting Services – Business Card</title>
<link rel="stylesheet" href="https://fonts.googleapis.com/css2?family=Tinos&display=swap">
<style>
  :root {
    --brand-green: #6fe21c;
    --ink: #000000;
    --paper: #ffffff;
  }
  html, body {
    margin: 0;
    padding: 0;
    width: 769px;
    height: 1200px;
    overflow: hidden;
    background: var(--paper);
  }
  .card {
    position: relative;
    width: 769px;
    height: 1200px;
    background: var(--paper);
    font-family: "Tinos", "Times New Roman", serif;
    color: var(--ink);
  }
  .business-name {
    position: absolute;
    top: 342px;
    left: 0;
    width: 769px;
    margin: 0;
    text-align: center;
    font-weight: 400;
    font-size: 36px;
    line-height: 1;
    letter-spacing: -1.2px;
    color: var(--brand-green);
    transform: scaleX(0.9);
    transform-origin: center;
    white-space: nowrap;
  }
  .principal {
    position: absolute;
    top: 740px;
    left: 380px;
    margin: 0;
    font-weight: 400;
    font-size: 34px;
    line-height: 1;
    white-space: nowrap;
  }
  .principal-rule {
    position: absolute;
    top: 798px;
    left: 364px;
    width: 350px;
    height: 3px;
    background: var(--brand-green);
  }
  .contact-line {
    position: absolute;
    margin: 0;
    font-size: 31px;
    line-height: 1;
    white-space: nowrap;
  }
  .contact-abn    { top: 886px;  left: 380px; }
  .contact-post   { top: 937px;  left: 178px; }
  .contact-mobile { top: 988px;  left: 380px; }
  .contact-email  { top: 1033px; left: 120px; }
</style>
</head>
<body>
  <main class="card">
    <h1 class="business-name">DESMOND HALVERTON CONSULTING SERVICES</h1>

    <p class="principal">Desmond Halverton</p>
    <div class="principal-rule"></div>

    <p class="contact-line contact-abn">ABN 37 818 502 194</p>
    <p class="contact-line contact-post">PO Box 871 KERRAWAY NSW 2619</p>
    <p class="contact-line contact-mobile">Mobile: 0431 558 906</p>
    <p class="contact-line contact-email">Email: desmond.halverton@quillmarsh.net</p>
  </main>
</body>
</html>
```